Plum & Us Business Card Design

Plum & Us is a company that makes treats and real food for people with food allergies, illnesses and those that like to eat clean. We like to take good old fashioned favorites and create a clean, healthy version of it without losing any of the addictive ‘yumminess’ of it.All of our products are made with Organic ingredients and we aim to be as sustainable as possible therefore I would like this to be reflected in our business cards. I like the thought of using chia seeds in the business card maybe so that people could grow their own.

Industry/Entity Type

Health And Wellness

Contact Information for Business Card

Plum & Uswww.plumandus.com.aumarnie@plumandus.com.auP: 0431 596 218 Facebook and Instagram logos

Requirements
Must have
• Logo - does not have to be the exact logo as long as it is close and fits in with the other information I have asked for (sustainable & Organic, recycled etc.)
• See the photo with the treats for a picture of the logo

```html
<!DOCTYPE html>
<html lang="en">
<head>
<meta charset="utf-8">
<title>Plum &amp; Us — Business Card</title>
<link rel="stylesheet" href="https://fonts.googleapis.com/css2?family=Montserrat:wght@400;500;600;700&display=swap">
<style>
  :root {
    --page: #ecebe8;
    --card: #ffffff;
    --panel-grey: #e6e6e6;
    --leaf-green: #9ccc2c;
    --leaf-green-dark: #86b61f;
    --ink: #222222;
    --ink-soft: #444444;
    --brand-navy: #2b2f7a;
    --seed-dark: #3b3733;
    --seed-mid: #7a726a;
    --icon-grey: #9a9a9a;
  }
  * { box-sizing: border-box; margin: 0; padding: 0; }
  html, body {
    width: 1200px; height: 913px; overflow: hidden;
    background: var(--page);
    font-family: "Montserrat", Arial, sans-serif;
    color: var(--ink);
  }
  .sheet {
    position: relative; width: 1200px; height: 913px;
  }
  .card {
    position: absolute; left: 290px;
    width: 620px; height: 379px;
    background: var(--card);
    border-radius: 16px;
    overflow: hidden;
    box-shadow: 0 6px 22px rgba(0,0,0,.12);
  }
  .card--front { top: 52px; }
  .card--back { top: 482px; }
  .card__shapes { position: absolute; inset: 0; }

  .seed-pile {
    position: absolute;
    border-radius: 50%;
    background: radial-gradient(ellipse at center, var(--seed-dark) 0%, var(--seed-mid) 55%, rgba(122,114,106,0) 72%);
  }
  .card--front .seed-pile { left: 380px; top: 48px; width: 180px; height: 100px; }
  .card--back .seed-pile { left: 420px; top: 40px; width: 170px; height: 95px; }

  .social {
    position: absolute; display: flex; gap: 6px;
  }
  .social__tile {
    width: 22px; height: 22px; border-radius: 4px;
    background: var(--icon-grey);
  }
  .card--front .social { right: 24px; top: 20px; }
  .card--back .social { right: 24px; top: 196px; }

  .brand {
    position: absolute; display: flex; align-items: center; gap: 8px;
    font-weight: 500; color: var(--brand-navy);
    letter-spacing: .5px;
  }
  .brand__dot {
    width: 12px; height: 12px; border-radius: 50%;
    background: var(--leaf-green);
  }
  .card--front .brand { left: 34px; top: 94px; font-size: 32px; }
  .card--back .brand { left: 44px; top: 122px; font-size: 36px; }

  .phone {
    position: absolute; display: flex; align-items: center; gap: 10px;
    font-weight: 600; font-size: 20px; color: var(--ink);
  }
  .card--front .phone { right: 34px; top: 170px; }
  .card--back .phone { left: 48px; top: 214px; }

  .contact {
    position: absolute; list-style: none;
    font-size: 12.5px; font-weight: 400; color: var(--ink-soft);
    line-height: 20px;
  }
  .contact li { display: flex; align-items: center; gap: 9px; }
  .card--front .contact { left: 200px; top: 300px; }
  .card--back .contact { left: 48px; top: 282px; }

  .icon { width: 14px; height: 14px; flex: none; }
  .icon--lg { width: 18px; height: 18px; }
</style>
</head>
<body>
<main class="sheet">

  <!-- Front of card -->
  <section class="card card--front" aria-label="Business card front">
    <svg class="card__shapes" viewBox="0 0 620 379" aria-hidden="true">
      <polygon points="0,72 262,72 236,150 0,150" fill="var(--panel-grey)"/>
      <polygon points="0,150 236,150 0,262" fill="var(--leaf-green)"/>
    </svg>

    <div class="seed-pile" role="img" aria-label="Photo of a small pile of chia seeds"></div>

    <div class="social" aria-label="Social links">
      <span class="social__tile"></span>
      <span class="social__tile"></span>
    </div>

    <div class="brand"><span class="brand__dot"></span>Plum &amp; Us</div>

    <div class="phone">
      <svg class="icon icon--lg" viewBox="0 0 20 20" aria-hidden="true">
        <circle cx="10" cy="10" r="9" fill="none" stroke="var(--ink)" stroke-width="1.6"/>
        <path d="M7 5.5l1.6 0 .8 2.4-1 .9a6 6 0 0 0 2.8 2.8l.9-1 2.4.8v1.6c0 .6-.5 1-1.1 1A7.5 7.5 0 0 1 6 6.6c0-.6.4-1.1 1-1.1z" fill="var(--ink)"/>
      </svg>
      <span>0431 596 218</span>
    </div>

    <ul class="contact">
      <li>
        <svg class="icon" viewBox="0 0 16 16" aria-hidden="true">
          <circle cx="8" cy="8" r="6.5" fill="none" stroke="var(--ink-soft)" stroke-width="1.4"/>
          <path d="M1.5 8h13M8 1.5c2.4 2.4 2.4 10.6 0 13M8 1.5c-2.4 2.4-2.4 10.6 0 13" fill="none" stroke="var(--ink-soft)" stroke-width="1.1"/>
        </svg>
        <span>www.plumandus.com.au</span>
      </li>
      <li>
        <svg class="icon" viewBox="0 0 16 16" aria-hidden="true">
          <circle cx="8" cy="8" r="6.5" fill="none" stroke="var(--ink-soft)" stroke-width="1.4"/>
          <rect x="4.5" y="5.5" width="7" height="5" fill="none" stroke="var(--ink-soft)" stroke-width="1"/>
          <path d="M4.5 5.5L8 8.5l3.5-3" fill="none" stroke="var(--ink-soft)" stroke-width="1"/>
        </svg>
        <span>marnie@plumandus.com.au</span>
      </li>
    </ul>
  </section>

  <!-- Back of card -->
  <section class="card card--back" aria-label="Business card back">
    <svg class="card__shapes" viewBox="0 0 620 379" aria-hidden="true">
      <polygon points="150,379 620,296 620,379" fill="var(--leaf-green)"/>
      <line x1="150" y1="379" x2="620" y2="296" stroke="var(--leaf-green-dark)" stroke-width="2"/>
    </svg>

    <div class="seed-pile" role="img" aria-label="Photo of a small pile of chia seeds"></div>

    <div class="social" aria-label="Social links">
      <span class="social__tile"></span>
      <span class="social__tile"></span>
    </div>

    <div class="brand"><span class="brand__dot"></span>Plum &amp; Us</div>

    <div class="phone">
      <svg class="icon icon--lg" viewBox="0 0 20 20" aria-hidden="true">
        <circle cx="10" cy="10" r="9" fill="none" stroke="var(--ink)" stroke-width="1.6"/>
        <path d="M7 5.5l1.6 0 .8 2.4-1 .9a6 6 0 0 0 2.8 2.8l.9-1 2.4.8v1.6c0 .6-.5 1-1.1 1A7.5 7.5 0 0 1 6 6.6c0-.6.4-1.1 1-1.1z" fill="var(--ink)"/>
      </svg>
      <span>0431 596 218</span>
    </div>

    <ul class="contact">
      <li>
        <svg class="icon" viewBox="0 0 16 16" aria-hidden="true">
          <circle cx="8" cy="8" r="6.5" fill="none" stroke="var(--ink-soft)" stroke-width="1.4"/>
          <path d="M1.5 8h13M8 1.5c2.4 2.4 2.4 10.6 0 13M8 1.5c-2.4 2.4-2.4 10.6 0 13" fill="none" stroke="var(--ink-soft)" stroke-width="1.1"/>
        </svg>
        <span>www.plumandus.com.au</span>
      </li>
      <li>
        <svg class="icon" viewBox="0 0 16 16" aria-hidden="true">
          <circle cx="8" cy="8" r="6.5" fill="none" stroke="var(--ink-soft)" stroke-width="1.4"/>
          <rect x="4.5" y="5.5" width="7" height="5" fill="none" stroke="var(--ink-soft)" stroke-width="1"/>
          <path d="M4.5 5.5L8 8.5l3.5-3" fill="none" stroke="var(--ink-soft)" stroke-width="1"/>
        </svg>
        <span>marnie@plumandus.com.au</span>
      </li>
    </ul>
  </section>

</main>
</body>
</html>
```